Brightvantage.com tech company website

Current site is www.brightvantage.com. The site will tell you about our company.

Designs we like are:
http://megainfo.quellorix.com
www.trelvo.com
www.morvasket.com

Target Market(s)

B2B

Industry/Entity Type

It Company

Coding

Coded - Design and coding required

Number of Pages Required

5+ page

Requirements
Must have
• We want to entice without giving away too much info. We like graphics and colors. But website must look official and credible.

```html
<!DOCTYPE html>
<html lang="en">
<head>
<meta charset="utf-8">
<title>Brightvantage</title>
<link rel="stylesheet" href="https://fonts.googleapis.com/css2?family=Open+Sans:wght@400;600;700&display=swap">
<style>
:root{
  --navy:#0c1d3a;
  --navy-deep:#07111f;
  --blue:#1f6db4;
  --blue-light:#4aa3e6;
  --accent:#f0a22e;
  --black:#050608;
  --graphite:#2b2c2f;
  --text:#333;
  --muted:#8a8f96;
  --white:#fff;
}
*{box-sizing:border-box;margin:0;padding:0}
html,body{width:700px;height:1200px;overflow:hidden;background:var(--white);font-family:"Open Sans",Arial,sans-serif;color:var(--text)}
.page{width:700px;height:1200px;position:relative;overflow:hidden}

/* header */
.site-header{height:80px;position:relative;background:var(--white)}
.brand{position:absolute;left:22px;top:26px;display:flex;align-items:center;gap:7px;white-space:nowrap}
.brand-mark{width:12px;height:12px;background:var(--blue);border-radius:50%;flex:none}
.brand-name{font-weight:700;font-size:15px;color:var(--navy);letter-spacing:.4px}
.main-nav{position:absolute;left:200px;right:0;top:0;height:32px;background:var(--navy);display:flex;align-items:center;justify-content:space-around;padding:0 8px}
.main-nav a{color:var(--white);font-size:7.5px;font-weight:600;text-decoration:none;letter-spacing:.3px;text-transform:uppercase;white-space:nowrap}
.header-contacts{position:absolute;right:24px;top:44px;display:flex;gap:34px}
.contact-chip{display:flex;align-items:center;gap:7px}
.contact-chip .icon{width:24px;height:24px;border-radius:50%;background:var(--blue);display:flex;align-items:center;justify-content:center}
.contact-chip small{display:block;font-size:7px;color:var(--muted);text-transform:uppercase}
.contact-chip span{font-size:9px;color:var(--navy);font-weight:600}

/* hero */
.hero{position:relative;height:375px}
.hero-photo{position:absolute;inset:0;background:linear-gradient(115deg,#1b2433 0%,#3d5d80 35%,#7fa6c9 55%,#2c4d72 80%,#10213a 100%)}
.hero-panel{position:absolute;right:0;top:70px;width:330px;height:125px;background:rgba(6,18,38,.55);padding:18px 26px}
.hero-panel h1{color:var(--white);font-size:24px;font-weight:600;line-height:1.25;letter-spacing:1px;text-transform:uppercase;text-align:right}
.slider-dots{position:absolute;right:52px;bottom:26px;display:flex;gap:6px}
.slider-dots i{width:14px;height:4px;background:rgba(255,255,255,.45)}
.slider-dots i.on{background:var(--white)}

/* services */
.services{position:relative;height:125px;background:var(--black);display:flex;padding:0 30px}
.service{flex:1;text-align:center;color:var(--white);padding:0 8px}
.service-icon{width:42px;height:42px;border-radius:50%;background:var(--blue);margin:-21px auto 8px;display:flex;align-items:center;justify-content:center;border:3px solid var(--black)}
.service h3{font-size:10px;font-weight:600;margin-bottom:5px}
.service p{font-size:7.5px;color:#b9bec6;line-height:1.4;margin-bottom:6px}
.service a{font-size:7.5px;color:var(--white);font-weight:700;text-decoration:none}
.services .arrow{position:absolute;top:52px}
.services .arrow.left{left:10px}.services .arrow.right{right:10px}

/* welcome */
.welcome{height:190px;text-align:center;padding:34px 70px 0}
.welcome h2{font-size:24px;font-weight:600;color:var(--graphite)}
.welcome h2 em{font-style:normal;color:var(--blue)}
.welcome p{font-size:8px;color:var(--muted);line-height:1.6;margin:12px 0 16px}
.btn{display:inline-block;background:var(--blue);color:var(--white);font-size:8px;font-weight:700;padding:8px 18px;text-transform:uppercase;letter-spacing:.5px}

/* case studies */
.case-row{display:flex;height:180px}
.team-photo{width:340px;background:linear-gradient(160deg,#7fb1e0 0%,#3d78b8 50%,#1d3f6e 100%)}
.case-studies{flex:1;background:var(--graphite);padding:20px 28px;color:var(--white)}
.case-studies h2{font-size:16px;font-weight:600;text-align:center;margin-bottom:12px}
.case-studies h2 em{font-style:normal;color:var(--accent)}
.case-list{list-style:none}
.case-list li{font-size:8px;line-height:1.9;padding-left:12px;position:relative;color:#e4e6ea}
.case-list li::before{content:"";position:absolute;left:0;top:6px;width:4px;height:4px;background:var(--white);border-radius:50%}

/* footer */
.site-footer{height:210px;background:var(--navy-deep);display:flex;padding:30px 50px 0}
.footer-col{flex:1;color:var(--white)}
.footer-col h2{font-size:18px;font-weight:400;color:var(--blue-light);margin-bottom:12px}
.contact-col{text-align:center}
.contact-col p{font-size:10px;line-height:1.6}
.socials{display:flex;justify-content:center;gap:8px;margin-top:10px}
.socials i{width:20px;height:20px;border-radius:50%;background:var(--blue)}
.newsletter p{font-size:8px;color:#b9bec6;line-height:1.5;margin-bottom:12px}
.field{width:200px;height:24px;background:#141c2a;border:1px solid #2a3548;font-size:8px;color:var(--muted);padding:6px 10px;margin-bottom:8px}
.newsletter .btn{width:200px;text-align:center}
.bottom-bar{height:40px;background:#0f1624;display:flex;justify-content:space-between;align-items:center;padding:0 22px;font-size:7.5px;color:#aab0b9}
</style>
</head>
<body>
<div class="page">
  <header class="site-header">
    <div class="brand"><span class="brand-mark"></span><span class="brand-name">BRIGHTVANTAGE</span></div>
    <nav class="main-nav">
      <a href="#">Home</a><a href="#">About</a><a href="#">Big Data and Analytics</a><a href="#">Perception and Branding</a><a href="#">Case Studies</a><a href="#">Contact</a>
    </nav>
    <div class="header-contacts">
      <div class="contact-chip">
        <span class="icon"><svg width="12" height="9" viewBox="0 0 12 9"><rect x=".5" y=".5" width="11" height="8" fill="none" stroke="#fff"/><path d="M.5 .5 6 5l5.5-4.5" fill="none" stroke="#fff"/></svg></span>
        <div><small>Email us</small><span>hello@brightvantage.com</span></div>
      </div>
      <div class="contact-chip">
        <span class="icon"><svg width="11" height="11" viewBox="0 0 24 24"><path fill="#fff" d="M6.6 10.8a15 15 0 0 0 6.6 6.6l2.2-2.2a1 1 0 0 1 1-.25 11 11 0 0 0 3.6.6 1 1 0 0 1 1 1V20a1 1 0 0 1-1 1A17 17 0 0 1 3 4a1 1 0 0 1 1-1h3.5a1 1 0 0 1 1 1c0 1.25.2 2.45.6 3.6a1 1 0 0 1-.25 1z"/></svg></span>
        <div><small>Call us</small><span>1-555-010-2040</span></div>
      </div>
    </div>
  </header>

  <section class="hero">
    <div class="hero-photo" role="img" aria-label="Business person in a suit touching a glowing digital screen"></div>
    <div class="hero-panel"><h1>Brightvantage is expert at data collection and analysis</h1></div>
    <div class="slider-dots"><i class="on"></i><i></i></div>
  </section>

  <section class="services">
    <svg class="arrow left" width="8" height="12" viewBox="0 0 8 12"><path d="M7 0 0 6l7 6z" fill="#fff"/></svg>
    <div class="service">
      <div class="service-icon"><svg width="18" height="18" viewBox="0 0 18 18"><circle cx="9" cy="9" r="7" fill="none" stroke="#fff" stroke-width="1.6"/><circle cx="9" cy="9" r="3" fill="#fff"/></svg></div>
      <h3>Truly Targeted Marketing</h3>
      <p>Reach the right buyers with clear, data led campaigns built for growth.</p>
      <a href="#">MORE &rsaquo;</a>
    </div>
    <div class="service">
      <div class="service-icon"><svg width="18" height="18" viewBox="0 0 18 18"><circle cx="9" cy="9" r="7" fill="none" stroke="#fff" stroke-width="1.6"/><path d="M9 1v16M1 9h16" stroke="#fff" stroke-width="1.6"/></svg></div>
      <h3>Lead Generation</h3>
      <p>Fill your pipeline with qualified prospects ready to start a talk.</p>
      <a href="#">MORE &rsaquo;</a>
    </div>
    <div class="service">
      <div class="service-icon"><svg width="18" height="18" viewBox="0 0 18 18"><path d="M2 16V10M7 16V6M12 16V8M16 16V3" stroke="#fff" stroke-width="2"/></svg></div>
      <h3>Data Enhancement</h3>
      <p>Clean, enrich and verify records so every decision rests on facts.</p>
      <a href="#">MORE &rsaquo;</a>
    </div>
    <div class="service">
      <div class="service-icon"><svg width="18" height="18" viewBox="0 0 18 18"><circle cx="9" cy="9" r="7" fill="none" stroke="#fff" stroke-width="1.6"/><path d="M9 4v10M6.5 6.5h4a1.5 1.5 0 0 1 0 3h-3a1.5 1.5 0 0 0 0 3h4" fill="none" stroke="#fff" stroke-width="1.4"/></svg></div>
      <h3>Data Monetization</h3>
      <p>Turn your data assets into steady new revenue with secure tools.</p>
      <a href="#">MORE &rsaquo;</a>
    </div>
    <svg class="arrow right" width="8" height="12" viewBox="0 0 8 12"><path d="M1 0l7 6-7 6z" fill="#fff"/></svg>
  </section>

  <section class="welcome">
    <h2>Welcome to <em>BRIGHTVANTAGE</em></h2>
    <p>We help business teams collect, connect and understand the data that drives their markets. Our analysts and engineers turn raw signals into clear insight, so your brand can plan with confidence, spend with purpose and grow with measurable results across every channel you serve today.</p>
    <span class="btn">Read More</span>
  </section>

  <section class="case-row">
    <div class="team-photo" role="img" aria-label="Silhouettes of a business team in front of a blue world map"></div>
    <div class="case-studies">
      <h2><em>CASE</em> STUDIES</h2>
      <ul class="case-list">
        <li>Raised market share for a national retail group</li>
        <li>Launched public offering outreach for a finance firm</li>
        <li>Grew online sales with precise audience targeting</li>
        <li>Built a custom data solution for a leading brand</li>
        <li>Delivered risk insight for a regional supply chain</li>
        <li>Improved reporting speed for a media network</li>
        <li>Sustained growth program for a high profile client</li>
      </ul>
    </div>
  </section>

  <footer class="site-footer">
    <div class="footer-col contact-col">
      <h2>Contact Us</h2>
      <p>CALL TOLL FREE<br>1-555-010-2040<br>No.1, Harbor Lane<br>Suite 12, 40521</p>
      <div class="socials"><i></i><i></i><i></i></div>
    </div>
    <div class="footer-col newsletter">
      <h2>News Letter Signup</h2>
      <p>Get fresh insight and company news sent to your inbox once each month.</p>
      <div class="field">Email Address</div>
      <span class="btn">Subscribe</span>
    </div>
  </footer>
  <div class="bottom-bar">
    <span>Policy &nbsp;|&nbsp; Privacy &nbsp;|&nbsp; Terms &amp; Condition</span>
    <span>Copyright &copy; 2024 Brightvantage. All rights reserved.</span>
  </div>
</div>
</body>
</html>
```